Super elegant, crisp & clean Business card design required

We recently upgraded our branding - which is on our website - tavorelstudio.com

I would like a simple, yet elegant, clean business card design please.

The font of my logo is Cinzel - and because of the natural colour - it's best to have this on a black background.

I would like to have the back of the business card - with simply my logo.

PLEASE DO NOT SUBMIT A COMPLICATED / UNCLEAN DESIGN

Industry/Entity Type

Business

Contact Information for Business Card

Dalvik Ostrander Photography

Font styles to use
Other font styles liked:
• Cinzel

Requirements
Must have
• A backpage with nothing but my logo
• Simple design - stands out
Should not have
• Colour that dont align with my logo
• Over complicated '/ non symmetrical design

```html
<!DOCTYPE html>
<html lang="en">
<head>
<meta charset="utf-8">
<title>Dalvik Ostrander Photography – Business Card</title>
<link rel="stylesheet" href="https://fonts.googleapis.com/css2?family=Cinzel:wght@400;700&display=swap">
<style>
  :root {
    --canvas-bg: #151515;
    --card-bg: #050505;
    --card-edge: #1e1e1e;
    --gold: #b9a47c;
    --gold-soft: #a8946d;
  }
  * { margin: 0; padding: 0; box-sizing: border-box; }
  html, body {
    width: 1200px;
    height: 1200px;
    overflow: hidden;
    background: var(--canvas-bg);
  }
  .canvas {
    position: relative;
    width: 1200px;
    height: 1200px;
    font-family: "Cinzel", serif;
    color: var(--gold);
  }
  .card {
    position: absolute;
    left: 190px;
    width: 820px;
    height: 470px;
    background: radial-gradient(ellipse at 40% 40%, #0c0c0c 0%, var(--card-bg) 70%);
    border: 1px solid var(--card-edge);
    box-shadow: 0 18px 40px rgba(0, 0, 0, 0.6);
  }
  .card--back { top: 90px; }
  .card--front { top: 640px; }

  .brand {
    display: flex;
    align-items: center;
    gap: 16px;
  }
  .brand__mark {
    width: 22px;
    height: 22px;
    border-radius: 50%;
    background: var(--gold);
    flex: none;
  }
  .brand__name {
    font-weight: 400;
    font-size: 34px;
    letter-spacing: 1px;
    color: var(--gold);
    white-space: nowrap;
  }
  .card--back .brand {
    position: absolute;
    top: 50%;
    left: 50%;
    transform: translate(-50%, -50%);
  }
  .card--front .brand {
    position: absolute;
    top: 120px;
    left: 60px;
  }
  .card--front .brand__name { font-size: 28px; }

  .contact {
    position: absolute;
    right: 60px;
    bottom: 50px;
    text-align: right;
    list-style: none;
  }
  .contact__item + .contact__item { margin-top: 26px; }
  .contact__label {
    display: block;
    font-weight: 700;
    font-size: 16px;
    letter-spacing: 0.5px;
    color: var(--gold);
  }
  .contact__value {
    display: block;
    font-weight: 400;
    font-size: 18px;
    letter-spacing: 0.5px;
    color: var(--gold-soft);
    margin-top: 2px;
  }
</style>
</head>
<body>
  <main class="canvas">
    <section class="card card--back" aria-label="Card back">
      <div class="brand">
        <span class="brand__mark"></span>
        <span class="brand__name">Dalvik Ostrander Photography</span>
      </div>
    </section>

    <section class="card card--front" aria-label="Card front">
      <div class="brand">
        <span class="brand__mark"></span>
        <span class="brand__name">Dalvik Ostrander Photography</span>
      </div>
      <ul class="contact">
        <li class="contact__item">
          <span class="contact__label">Phone Number</span>
          <span class="contact__value">07700914382</span>
        </li>
        <li class="contact__item">
          <span class="contact__label">Website</span>
          <span class="contact__value">tavorelstudio.com</span>
        </li>
        <li class="contact__item">
          <span class="contact__label">Email Address</span>
          <span class="contact__value">mail@tavorelstudio.com</span>
        </li>
      </ul>
    </section>
  </main>
</body>
</html>
```